Accident Law Firm Billboard Bold Easy to See Car Accidents

We need a billboard design that can catch attention in a very crowed Car Accident lawyer market. We wish to feature the phone number (652) 318-4470 as the focus of the Bill Board. We are trying to get the phone number recognized and remembered by drivers. The law firm name is not as crucial to remember.
Basically, It's CAR ACCIDENT? Then (652) 318-4470. We are not married to any specific color scheme but it has to POP and catch attention.
So the Crucial elements are as follows:
1. Phone number (652) 318-4470
2. Words CAR ACCIDENT?
3. Firm Logo in lower portion or where appropriate. Firm Logo to be provided
4. We may want to try a Day Glow orange color, with White and Black added. An example of the color scheme shall be provided.
5. Possible "Catch Phrase" to be used, "It's Time Call 9"
Target Market(s)
Orlando Florida Car Accident victims
Industry/Entity Type
Law Firm
Requirements
Must have
- Easy to see phone number (652) 318-4470
- Catch attention
Nice to have
- I would like to have the sign visible in bright sunlight and it not too hard to immediately know what phone number is for
Should not have
- too many words
- No bold enough
- confusing fonts
- Unclear fonts

```html
<!DOCTYPE html>
<html lang="en">
<head>
<meta charset="utf-8">
<title>Marbrook Law Firm P.C. – Car Accident Billboard</title>
<link rel="stylesheet" href="https://fonts.googleapis.com/css2?family=Spectral:wght@700;800&display=swap">
<style>
  :root {
    --day-glow-orange: #f68b4b;
    --ink: #262626;
  }
  html, body {
    margin: 0;
    padding: 0;
    overflow: hidden;
    background: var(--day-glow-orange);
  }
  .billboard {
    position: relative;
    width: 1200px;
    height: 270px;
    background: var(--day-glow-orange);
    color: var(--ink);
    font-family: "Spectral", Georgia, serif;
    overflow: hidden;
  }
  .firm-name {
    position: absolute;
    left: 55px;
    top: 78px;
    margin: 0;
    font-weight: 800;
    line-height: 1;
    color: var(--ink);
  }
  .firm-name__main {
    display: block;
    font-size: 34px;
    letter-spacing: 0.02em;
  }
  .firm-name__sub {
    display: block;
    font-size: 18px;
    letter-spacing: 0.17em;
    margin-top: 2px;
  }
  .headline {
    position: absolute;
    left: 340px;
    width: 860px;
    top: 22px;
    margin: 0;
    text-align: center;
    font-weight: 800;
    font-size: 62px;
    line-height: 1;
    letter-spacing: 0.02em;
  }
  .call-line {
    position: absolute;
    left: 372px;
    top: 102px;
    margin: 0;
    height: 84px;
    display: flex;
    align-items: center;
    gap: 22px;
    font-weight: 800;
    font-size: 66px;
    line-height: 1;
    white-space: nowrap;
  }
  .call-line__mark {
    width: 82px;
    height: 82px;
    flex: none;
  }
  .tagline {
    position: absolute;
    left: 340px;
    width: 810px;
    top: 208px;
    margin: 0;
    text-align: center;
    font-weight: 700;
    font-size: 22px;
    line-height: 1.2;
    letter-spacing: 0.32em;
  }
</style>
</head>
<body>
  <main class="billboard">
    <p class="firm-name">
      <span class="firm-name__main">MARBROOK</span>
      <span class="firm-name__sub">LAW FIRM P.C.</span>
    </p>

    <h1 class="headline">CAR ACCIDENT?</h1>

    <p class="call-line">
      <span>call us</span>
      <svg class="call-line__mark" viewBox="0 0 82 82" aria-hidden="true">
        <circle cx="41" cy="41" r="35" fill="none" stroke="var(--ink)" stroke-width="8"/>
      </svg>
      <span class="call-line__number">(652) 318-4470</span>
    </p>

    <p class="tagline">It's Time Call 9</p>
  </main>
</body>
</html>
```